Control panel UI redesign for a learning simulation

Hello. I'm producing a learning simulation and need help with designing a control panel. You will see the panel on the bottom of the image. The look, colors, size, placement, etc. can change, but it has to remain horizontal, that's my only requirement. Overall, I'm open to suggestions. Thank you for your help!

NOTE: the last two items (success rate and progress) are indicators, not buttons, so they should look different from the buttons.

Industry/Entity Type

Learning

Other font styles liked:
• Open Sans

```html
<!DOCTYPE html>
<html lang="en">
<head>
<meta charset="utf-8">
<title>Simulation Control Panel</title>
<link href="https://fonts.googleapis.com/css2?family=Open+Sans:wght@300;400;600&display=swap" rel="stylesheet">
<style>
  :root{
    --bg:#ffffff;
    --bar-bg:#f6f6f6;
    --ring-bg:#efefef;
    --ring-edge:#dedede;
    --blue:#4a8ee0;
    --grey-icon:#8c8c8c;
    --dark:#3b3b3b;
    --heading:#444444;
    --less:#d0021b;
    --less-edge:#e07f6a;
    --high:#7cb342;
    --high-edge:#9cc06c;
    --medium:#c55a22;
    --medium-edge:#c8693a;
    --map-a:#e9e9e9;
    --map-b:#f1efe8;
  }
  *{box-sizing:border-box;margin:0;padding:0}
  html,body{width:1200px;height:800px;overflow:hidden;background:var(--bg);font-family:'Open Sans',sans-serif}
  .canvas{position:relative;width:1200px;height:800px}
  .abs{position:absolute}

  .map-area{left:36px;top:0;width:454px;height:210px;
    background:linear-gradient(135deg,var(--map-a),var(--map-b));
    box-shadow:0 2px 4px rgba(0,0,0,.25)}

  .bar{position:absolute;background:var(--bar-bg);border:1px solid}
  .bar--less{border-color:var(--less-edge)}
  .bar--high{border-color:var(--high-edge)}
  .bar--medium{border-color:var(--medium-edge)}

  .progress-label{position:absolute;background:var(--blue);color:#fff;font-weight:400;
    display:flex;align-items:center;justify-content:center;white-space:nowrap}

  .nav-btn{position:absolute;background:var(--dark);color:#fff;display:flex;align-items:center;justify-content:center;font-weight:400}

  .rate{position:absolute}
  .rate svg{display:block}
  .rate-text{position:absolute;inset:0;display:flex;flex-direction:column;align-items:center;justify-content:center;color:#fff;line-height:1.1}
  .rate-level{border-bottom:1px solid #fff;padding:0 4px;letter-spacing:.5px;font-weight:400}

  .icon{position:absolute;transform:translate(-50%,-50%);overflow:visible}
  .icon--inactive{color:var(--grey-icon)}
  .icon--active{color:var(--blue)}

  .sheet-title{position:absolute;color:var(--heading);font-weight:300;font-size:27px;line-height:1}
  .sheet-rule{position:absolute;height:2px;background:var(--heading)}
</style>
</head>
<body>
<svg width="0" height="0" style="position:absolute">
  <defs>
    <symbol id="ic-pin" viewBox="0 0 100 100">
      <path d="M50 95 C40 78 18 58 18 38 A32 32 0 0 1 82 38 C82 58 60 78 50 95Z" fill="none" stroke="currentColor" stroke-width="4"/>
    </symbol>
    <symbol id="ic-bookmark" viewBox="0 0 100 100">
      <rect x="18" y="4" width="64" height="10" fill="var(--cap, none)"/>
      <path d="M20 6 H80 V94 L50 64 L20 94Z" fill="none" stroke="currentColor" stroke-width="4"/>
    </symbol>
    <symbol id="ic-doc" viewBox="0 0 100 100">
      <path d="M22 6 H68 L80 18 V94 H22Z" fill="none" stroke="currentColor" stroke-width="4"/>
      <path d="M68 6 V18 H80" fill="none" stroke="currentColor" stroke-width="3"/>
      <g stroke="currentColor" stroke-width="2.5">
        <line x1="32" y1="22" x2="64" y2="22"/><line x1="32" y1="29" x2="70" y2="29"/>
        <line x1="32" y1="36" x2="70" y2="36"/><line x1="32" y1="43" x2="70" y2="43"/>
        <line x1="32" y1="50" x2="70" y2="50"/><line x1="32" y1="57" x2="70" y2="57"/>
      </g>
      <rect x="32" y="66" width="38" height="18" fill="none" stroke="currentColor" stroke-width="3"/>
    </symbol>
    <symbol id="ic-at" viewBox="0 0 100 100">
      <text x="50" y="74" font-family="Open Sans, sans-serif" font-size="88" text-anchor="middle" fill="currentColor">@</text>
      <line x1="30" y1="94" x2="70" y2="94" stroke="currentColor" stroke-width="4"/>
    </symbol>
    <symbol id="ic-chat" viewBox="0 0 100 100">
      <path d="M8 14 H92 V70 H42 L24 88 V70 H8Z" fill="none" stroke="currentColor" stroke-width="4"/>
      <g fill="var(--dots, none)" stroke="var(--dot-line, currentColor)" stroke-width="2.5">
        <circle cx="34" cy="42" r="5"/><circle cx="50" cy="42" r="5"/><circle cx="66" cy="42" r="5"/>
      </g>
    </symbol>
    <symbol id="ic-pen" viewBox="0 0 100 100">
      <path d="M20 86 L26 68 L78 14 L90 26 L38 80Z" fill="currentColor"/>
      <line x1="14" y1="92" x2="62" y2="92" stroke="var(--base, currentColor)" stroke-width="4"/>
    </symbol>
  </defs>
</svg>

<div class="canvas">
  <div class="abs map-area" role="img" aria-label="Street map of the simulation area"></div>

  <!-- Compact panel -->
  <div class="bar bar--less" style="left:148px;top:248px;width:293px;height:43px"></div>
  <div class="progress-label" style="left:148px;top:235px;width:70px;height:13px;font-size:8px">25 % Completed</div>
  <div class="nav-btn" style="left:356px;top:293px;width:42px;height:12px;font-size:9px">Back</div>
  <div class="nav-btn" style="left:399px;top:293px;width:42px;height:12px;font-size:9px">Next</div>
  <svg class="icon icon--active" width="26" height="28" style="left:182px;top:270px"><use href="#ic-pin"/></svg>
  <svg class="icon icon--inactive" width="26" height="28" style="left:228px;top:270px"><use href="#ic-bookmark"/></svg>
  <svg class="icon icon--inactive" width="26" height="28" style="left:275px;top:270px"><use href="#ic-doc"/></svg>
  <svg class="icon icon--inactive" width="26" height="28" style="left:321px;top:270px"><use href="#ic-at"/></svg>
  <svg class="icon icon--inactive" width="26" height="28" style="left:368px;top:270px"><use href="#ic-chat"/></svg>
  <svg class="icon icon--inactive" width="26" height="28" style="left:415px;top:270px"><use href="#ic-pen"/></svg>
  <div class="rate" style="left:86px;top:234px;width:68px;height:68px">
    <svg width="68" height="68" viewBox="0 0 68 68">
      <circle cx="34" cy="34" r="33.5" fill="var(--ring-bg)" stroke="var(--ring-edge)"/>
      <circle cx="34" cy="34" r="31.5" fill="none" stroke="var(--blue)" stroke-width="5" stroke-dasharray="49.5 200" transform="rotate(-90 34 34)"/>
      <circle cx="34" cy="34" r="29" fill="var(--less)"/>
    </svg>
    <div class="rate-text"><span class="rate-level" style="font-size:11px">LESS</span><span style="font-size:7.5px">Success Rate</span></div>
  </div>

  <!-- High panel -->
  <div class="bar bar--high" style="left:184px;top:454px;width:560px;height:82px"></div>
  <div class="progress-label" style="left:178px;top:430px;width:139px;height:23px;font-size:16px">25 % Completed</div>
  <div class="nav-btn" style="left:582px;top:540px;width:80px;height:22px;font-size:17px">Back</div>
  <div class="nav-btn" style="left:664px;top:540px;width:80px;height:22px;font-size:17px">Next</div>
  <svg class="icon icon--active" width="50" height="52" style="left:248px;top:496px"><use href="#ic-pin"/></svg>
  <svg class="icon icon--inactive" width="50" height="52" style="left:337px;top:496px"><use href="#ic-bookmark"/></svg>
  <svg class="icon icon--inactive" width="50" height="52" style="left:426px;top:496px"><use href="#ic-doc"/></svg>
  <svg class="icon icon--inactive" width="50" height="52" style="left:515px;top:496px"><use href="#ic-at"/></svg>
  <svg class="icon icon--inactive" width="50" height="52" style="left:604px;top:496px"><use href="#ic-chat"/></svg>
  <svg class="icon icon--inactive" width="50" height="52" style="left:694px;top:496px"><use href="#ic-pen"/></svg>
  <div class="rate" style="left:64px;top:427px;width:138px;height:138px">
    <svg width="138" height="138" viewBox="0 0 138 138">
      <circle cx="69" cy="69" r="68.5" fill="var(--ring-bg)" stroke="var(--ring-edge)"/>
      <circle cx="69" cy="69" r="62.5" fill="none" stroke="var(--blue)" stroke-width="13" stroke-dasharray="98.2 400" transform="rotate(-90 69 69)"/>
      <circle cx="69" cy="69" r="56" fill="var(--high)"/>
    </svg>
    <div class="rate-text"><span class="rate-level" style="font-size:22px">HIGH</span><span style="font-size:15px">Success Rate</span></div>
  </div>

  <!-- Medium panel -->
  <div class="bar bar--medium" style="left:480px;top:635px;width:678px;height:95px"></div>
  <div class="progress-label" style="left:502px;top:610px;width:162px;height:25px;font-size:18px">50 % Completed</div>
  <div class="nav-btn" style="left:970px;top:735px;width:94px;height:26px;font-size:20px">Back</div>
  <div class="nav-btn" style="left:1066px;top:735px;width:92px;height:26px;font-size:20px">Next</div>
  <svg class="icon icon--active" width="60" height="62" style="left:585px;top:684px"><use href="#ic-pin"/></svg>
  <svg class="icon icon--inactive" width="60" height="62" style="left:687px;top:684px"><use href="#ic-bookmark"/></svg>
  <svg class="icon icon--inactive" width="60" height="62" style="left:790px;top:684px"><use href="#ic-doc"/></svg>
  <svg class="icon icon--inactive" width="60" height="62" style="left:894px;top:684px"><use href="#ic-at"/></svg>
  <svg class="icon icon--inactive" width="60" height="62" style="left:996px;top:684px"><use href="#ic-chat"/></svg>
  <svg class="icon icon--inactive" width="60" height="62" style="left:1100px;top:684px"><use href="#ic-pen"/></svg>
  <div class="rate" style="left:374px;top:606px;width:156px;height:156px">
    <svg width="156" height="156" viewBox="0 0 156 156">
      <circle cx="78" cy="78" r="77.5" fill="var(--ring-bg)" stroke="var(--ring-edge)"/>
      <circle cx="78" cy="78" r="72" fill="none" stroke="var(--blue)" stroke-width="12" stroke-dasharray="226.2 500" transform="rotate(-90 78 78)"/>
      <circle cx="78" cy="78" r="66" fill="var(--medium)"/>
    </svg>
    <div class="rate-text"><span class="rate-level" style="font-size:27px">MEDIUM</span><span style="font-size:18px">Success Rate</span></div>
  </div>

  <!-- Icon sheet: inactive -->
  <div class="sheet-title" style="left:808px;top:44px">Inactive Icons</div>
  <div class="sheet-rule" style="left:808px;top:73px;width:324px"></div>
  <svg class="icon icon--inactive" width="58" height="62" style="left:842px;top:134px"><use href="#ic-pin"/></svg>
  <svg class="icon icon--inactive" width="58" height="62" style="left:966px;top:134px"><use href="#ic-bookmark"/></svg>
  <svg class="icon icon--inactive" width="58" height="62" style="left:1091px;top:134px"><use href="#ic-doc"/></svg>
  <svg class="icon icon--inactive" width="58" height="62" style="left:842px;top:244px"><use href="#ic-at"/></svg>
  <svg class="icon icon--inactive" width="58" height="62" style="left:966px;top:244px"><use href="#ic-chat"/></svg>
  <svg class="icon icon--inactive" width="58" height="62" style="left:1091px;top:244px"><use href="#ic-pen"/></svg>

  <!-- Icon sheet: active -->
  <div class="sheet-title" style="left:810px;top:352px">Active icons</div>
  <div class="sheet-rule" style="left:810px;top:380px;width:296px"></div>
  <svg class="icon icon--active" width="58" height="62" style="left:832px;top:434px"><use href="#ic-pin"/></svg>
  <svg class="icon icon--active" width="58" height="62" style="left:958px;top:434px;--cap:var(--dark)"><use href="#ic-bookmark"/></svg>
  <svg class="icon icon--active" width="58" height="62" style="left:1082px;top:434px"><use href="#ic-doc"/></svg>
  <svg class="icon icon--active" width="58" height="62" style="left:838px;top:540px"><use href="#ic-at"/></svg>
  <svg class="icon icon--active" width="58" height="62" style="left:958px;top:540px;--dots:var(--dark);--dot-line:var(--dark)"><use href="#ic-chat"/></svg>
  <svg class="icon icon--active" width="58" height="62" style="left:1082px;top:540px;--base:var(--dark)"><use href="#ic-pen"/></svg>
</div>
</body>
</html>
```